Plumbing Truck design, emergency plumbing vehicle

Simple, highly effective plumbing design for plumbing vehicles

Brightwater Plumbing & Gas Services
(The Steadfast Pipe Professionals) moto

yellow, black and white colours (white as the vehicles are already painted white)

Clean and simple design

Attention grabbing

24hr Emergency service (listed on on the vehicle) possibly in red colour

Target Market(s)

plumbing

Industry/Entity Type

Plumbing

Colors
fbed22

Requirements
Must have
• Brightwater Plumbing & Gas Services
• (The Steadfast Pipe Professionals) moto
• yellow, black and white colours (white as the vehicles are already painted white)
• Clean and simple design
• Attention grabbing
• 24hr Emergency service (listed on on the vehicle) possibly in red colour
Should not have
• No plumbing symbols, pictures or icons

```html
<!DOCTYPE html>
<html lang="en">
<head>
<meta charset="utf-8">
<title>Brightwater Plumbing &amp; Gas Services – Vehicle Wrap Panels</title>
<link rel="stylesheet" href="https://fonts.googleapis.com/css2?family=Montserrat:wght@700;800&display=swap">
<style>
  :root{
    --yellow:#fbed22;
    --black:#0c0c0c;
    --white:#ffffff;
    --red:#d62631;
    --backdrop:#5c5c5c;
  }
  html,body{margin:0;padding:0;overflow:hidden;}
  body{width:1005px;height:1200px;background:var(--backdrop);}
  .wrap-sheet{display:block;width:1005px;height:1200px;}
  .fill-black{fill:var(--black);}
  .fill-yellow{fill:var(--yellow);}
  .fill-white{fill:var(--white);}
  .trim-line{fill:none;stroke:var(--white);stroke-width:2;}
  .panel-edge{fill:none;stroke:#b02a2a;stroke-width:0.8;}
  .brand-text{font-family:"Montserrat",sans-serif;font-weight:800;fill:var(--white);}
  .motto-text{font-family:"Montserrat",sans-serif;font-weight:700;fill:var(--white);letter-spacing:.3px;}
  .emergency-text{font-family:"Montserrat",sans-serif;font-weight:800;fill:var(--red);}
</style>
</head>
<body>
<svg class="wrap-sheet" viewBox="0 0 1005 1200" xmlns="http://www.w3.org/2000/svg" role="img" aria-label="Flat vehicle wrap panels for Brightwater Plumbing and Gas Services">
  <defs>
    <linearGradient id="halftone-tone" x1="0" y1="0" x2="0" y2="1">
      <stop offset="0" stop-color="#fbed22"/>
      <stop offset="1" stop-color="#c9bd10"/>
    </linearGradient>
    <clipPath id="clip-tray-driver"><path d="M0,5 L170,0 L170,138 L315,138 L315,205 L250,205 A48,48 0 0 0 155,205 L20,205 L0,180 Z"/></clipPath>
    <clipPath id="clip-cab"><path d="M5,15 L170,5 Q240,10 330,60 L445,80 Q475,88 475,115 L472,165 L430,195 A70,70 0 0 0 290,195 L10,195 L0,170 Z"/></clipPath>
    <clipPath id="clip-tray-passenger"><path d="M0,10 L300,0 L310,205 L160,205 A55,55 0 0 0 50,205 L0,205 Z"/></clipPath>
    <clipPath id="clip-rear"><path d="M0,0 L95,0 L95,90 L210,90 L210,0 L300,0 L300,190 L0,190 Z"/></clipPath>

    <g id="emergency-label">
      <text class="emergency-text" x="0" y="-3" font-size="16" text-anchor="middle">24HR EMERGENCY</text>
      <text class="emergency-text" x="0" y="15" font-size="16" text-anchor="middle">SERVICE</text>
    </g>

    <g id="cab-artwork">
      <g clip-path="url(#clip-cab)">
        <rect class="fill-black" width="480" height="200"/>
        <path class="fill-white" d="M0,0 L480,0 L480,100 L445,92 L330,70 Q240,22 170,18 L0,26 Z"/>
        <path class="fill-yellow" d="M0,125 L230,80 L250,95 L0,145 Z"/>
        <path class="fill-yellow" d="M330,95 L475,75 L475,100 L340,118 Z"/>
        <path fill="url(#halftone-tone)" d="M0,160 L475,100 L475,200 L0,200 Z" role="img" aria-label="Yellow halftone dot texture"/>
        <path class="fill-black" d="M0,188 L475,128 L475,142 L0,200 Z"/>
        <rect class="trim-line" x="30" y="30" width="205" height="48" rx="12"/>
      </g>
      <path class="panel-edge" d="M5,15 L170,5 Q240,10 330,60 L445,80 Q475,88 475,115 L472,165 L430,195 A70,70 0 0 0 290,195 L10,195 L0,170 Z"/>
    </g>

    <g id="brand-block">
      <rect class="fill-black" x="0" y="0" width="170" height="62" rx="3"/>
      <text class="brand-text" x="85" y="28" font-size="20" text-anchor="middle">BRIGHTWATER</text>
      <text class="brand-text" x="85" y="46" font-size="10" text-anchor="middle">PLUMBING &amp; GAS</text>
      <text class="brand-text" x="85" y="56" font-size="6" text-anchor="middle">SERVICES</text>
    </g>
  </defs>

  <g class="panel-row" transform="translate(35,150) scale(1.15)">
    <g class="tray-panel">
      <g clip-path="url(#clip-tray-driver)">
        <rect class="fill-black" width="320" height="210"/>
        <path class="fill-yellow" d="M0,0 L175,0 L175,30 L0,78 Z"/>
        <path class="fill-yellow" d="M0,112 L175,72 L175,100 L0,142 Z"/>
        <path fill="url(#halftone-tone)" d="M0,165 L320,118 L320,210 L0,210 Z" role="img" aria-label="Yellow halftone dot texture"/>
        <path class="fill-black" d="M0,192 L320,146 L320,160 L0,206 Z"/>
      </g>
      <path class="panel-edge" d="M0,5 L170,0 L170,138 L315,138 L315,205 L250,205 A48,48 0 0 0 155,205 L20,205 L0,180 Z"/>
      <use href="#emergency-label" transform="translate(86,22) scale(0.95)"/>
    </g>
    <g class="cab-panel" transform="translate(330,5)">
      <use href="#cab-artwork"/>
      <use href="#brand-block" transform="translate(155,110)"/>
    </g>
  </g>

  <g class="panel-row" transform="translate(35,480) scale(1.15)">
    <g class="cab-panel">
      <use href="#cab-artwork" transform="translate(475,0) scale(-1,1)"/>
      <use href="#brand-block" transform="translate(150,110)"/>
    </g>
    <g class="tray-panel" transform="translate(490,0)">
      <g clip-path="url(#clip-tray-passenger)">
        <rect class="fill-black" width="315" height="210"/>
        <path class="fill-yellow" d="M110,0 L315,0 L315,25 L150,40 Z"/>
        <path class="fill-yellow" d="M0,150 L315,70 L315,100 L0,180 Z"/>
        <path fill="url(#halftone-tone)" d="M0,190 L315,130 L315,210 L0,210 Z" role="img" aria-label="Yellow halftone dot texture"/>
      </g>
      <path class="panel-edge" d="M0,10 L300,0 L310,205 L160,205 A55,55 0 0 0 50,205 L0,205 Z"/>
      <g transform="translate(18,110) rotate(-16)">
        <text class="motto-text" x="0" y="0" font-size="12.5">THE STEADFAST</text>
        <text class="motto-text" x="-4" y="16" font-size="12.5">PIPE PROFESSIONALS</text>
      </g>
      <use href="#emergency-label" transform="translate(232,128) scale(0.92)"/>
    </g>
  </g>

  <g class="rear-panel" transform="translate(307,830) scale(1.3)">
    <g clip-path="url(#clip-rear)">
      <rect class="fill-black" width="300" height="190"/>
      <path class="fill-yellow" d="M0,0 L95,0 L95,20 L0,45 Z"/>
      <path class="fill-yellow" d="M210,0 L300,0 L300,30 L210,55 Z"/>
      <path class="fill-yellow" d="M0,70 L300,60 L300,82 L0,95 Z"/>
      <path fill="url(#halftone-tone)" d="M0,110 L300,105 L300,145 L0,150 Z" role="img" aria-label="Yellow halftone dot texture"/>
    </g>
    <path class="panel-edge" d="M0,0 L95,0 L95,90 L210,90 L210,0 L300,0 L300,190 L0,190 Z"/>
    <use href="#emergency-label" transform="translate(255,42) scale(0.55)"/>
    <use href="#brand-block" transform="translate(87,95) scale(0.75)"/>
    <text class="motto-text" x="150" y="174" font-size="5.5" text-anchor="middle">THE STEADFAST</text>
    <text class="motto-text" x="150" y="181" font-size="5.5" text-anchor="middle">PIPE PROFESSIONALS</text>
  </g>
</svg>
</body>
</html>
```